PostCard Design Project

I am making a mailing postcard
I am having the mailing printed using 4 color foil on certain parts.
I am looking for a design that maximizes the foil process where certain parts are done in foil to grab the customers attention (example: if there is a car on the postcard the headlights would be done in foil) .
I am targeting some industries, (auto, real estate, medical, beauty) I would like the post card to have examples of postcard ideas for 2 or 3 of these industries.
specs:
the postcard should be atleast 6.5x9 up to 8.5x11, I don't want to restrict the space for the creative as I don't want everything to look like a huge mess. both sides will be used.
the piece is a direct mail piece so it has to meet requirements of https://www.parcelvane-post.com/business/pdf/quick-reference-guide.pdf
text will be
"business with no limits, meet mailing with no addresses, gain new customers through "Whole Route Flyer Drop" reach new customers at their home without needing their address. "
I also want some current print specials I am running included.
-double your order FREE (order 500 business cards and get 1000)
-250 100lb gloss stock brochures 99.00
-business packages (cards, envelopes and letterhead) 299
-1000 flyers 140.40
-5000 postcards 179.99
A list of services
banners
booklets
brochures
business cards
calendars
catalogs
CD/DVD packages
envelopes
event tickets
flyers
hangtags
postcards
posters
presentation folders
rack cards
labels
table tents
window cling and decal
"order 24/7 orders@cardwillow.com" must be included
my logo is CardWillow will be supplied later
ive received some great designs. however Im looking for something a little more modern like some zelkor would put out. if the amount of words is too much please feel free to edit. also an idea i had for the list of services i offer is to have it transparent yet readable as the background of the postcard some small some big but covering the entire backgroud. you can then design on top of that with other thing. just an early morning thought
Reason: I have uploaded a sketch of my idea, please take time to look at it for an accurate depiction of what im looking for. feel free to add elements that make it pop off the page
Reason: We are getting close i will be providing feed back today
Business

```html
<!DOCTYPE html>
<html lang="en">
<head>
<meta charset="utf-8">
<title>CardWillow Postcard</title>
<link rel="stylesheet" href="https://fonts.googleapis.com/css2?family=Anton&family=Open+Sans:wght@400;600;700&family=Roboto+Condensed:wght@700&display=swap">
<style>
  :root {
    --backdrop: #e9e9e7;
    --card: #ffffff;
    --green: #8cc63e;
    --blue: #2b92d4;
    --red: #e5262c;
    --ink: #222222;
    --muted: #4a4a4a;
    --bubble: #e4e4e4;
    --logo: #2b8fcf;
  }
  * { box-sizing: border-box; margin: 0; padding: 0; }
  html, body { width: 839px; height: 1200px; overflow: hidden; }
  body { background: var(--backdrop); font-family: "Open Sans", Arial, sans-serif; color: var(--ink); position: relative; }

  .postcard { position: absolute; left: 81px; width: 667px; height: 481px; background: var(--card); box-shadow: 0 2px 6px rgba(0,0,0,.18); overflow: hidden; }
  .postcard--front { top: 92px; }
  .postcard--back { top: 618px; }

  /* Front */
  .headline { color: var(--green); }
  .headline__line { position: absolute; left: 20px; font-family: "Roboto Condensed", Arial, sans-serif; font-weight: 700; font-size: 40px; line-height: 40px; white-space: nowrap; }
  .headline__line--one { top: 24px; }
  .headline__line--two { top: 68px; }
  .headline__big { position: absolute; left: 20px; top: 104px; font-family: "Anton", "Roboto Condensed", sans-serif; font-weight: 400; font-size: 72px; line-height: 80px; letter-spacing: .5px; white-space: nowrap; }
  .brand { position: absolute; left: 436px; top: 22px; display: flex; align-items: center; gap: 7px; }
  .brand__dot { width: 22px; height: 22px; border-radius: 50%; background: var(--green); }
  .brand__name { font-family: "Open Sans", Arial, sans-serif; font-weight: 400; font-size: 27px; color: var(--logo); letter-spacing: -.5px; }
  .photo { position: absolute; }
  .photo--smile { left: 364px; top: 77px; width: 279px; height: 179px; background: linear-gradient(160deg, #f2d9cf 0%, #d9838a 45%, #b8324a 100%); }
  .photo--model { left: 126px; top: 195px; width: 238px; height: 182px; background: linear-gradient(120deg, #d6e4ee 0%, #e8cfc2 50%, #c9a590 100%); }
  .photo--car { left: 367px; top: 275px; width: 276px; height: 188px; background: linear-gradient(135deg, #d8232f 0%, #a8121c 45%, #2a2a2e 75%, #0f0f12 100%); }
  .contact { position: absolute; left: 20px; top: 389px; font-family: "Roboto Condensed", Arial, sans-serif; font-weight: 700; color: var(--green); font-size: 28px; line-height: 33px; white-space: nowrap; }

  /* Back */
  .pitch { position: absolute; left: 14px; top: 10px; color: var(--blue); font-weight: 700; font-size: 14.5px; line-height: 22px; white-space: nowrap; }
  .pitch__program { color: var(--green); }
  .indicia { position: absolute; left: 566px; top: 20px; width: 77px; height: 80px; border: 1px solid var(--ink); font-size: 8.5px; line-height: 1.3; text-align: center; padding-top: 9px; text-transform: uppercase; }
  .indicia__paid { font-size: 11px; }
  .indicia__route { text-transform: none; }
  .address { position: absolute; left: 488px; top: 112px; width: 155px; height: 77px; border: 1px solid var(--ink); padding: 20px 0 0 16px; font-size: 13px; line-height: 1.3; }

  .specials-title { position: absolute; left: 165px; top: 144px; color: var(--red); font-family: "Roboto Condensed", Arial, sans-serif; font-weight: 700; font-size: 23px; line-height: 22px; }
  .special { position: absolute; background: var(--bubble); border-radius: 14px; display: flex; align-items: center; justify-content: center; text-align: center; font-size: 12.5px; line-height: 1.6; color: var(--ink); padding: 2px; white-space: nowrap; }
  .special--double { left: 17px; top: 176px; width: 140px; height: 109px; }
  .special--brochures { left: 162px; top: 221px; width: 127px; height: 94px; }
  .special--packages { left: 17px; top: 294px; width: 143px; height: 109px; }
  .special--postcards { left: 168px; top: 323px; width: 108px; height: 94px; }
  .special--flyers { left: 90px; top: 399px; width: 90px; height: 60px; }

  .services { position: absolute; left: 315px; top: 72px; }
  .services__title { color: var(--red); font-weight: 400; font-size: 37px; line-height: 40px; }
  .services__list { list-style: none; }
  .services__item { font-weight: 600; font-size: 14.5px; line-height: 22.2px; color: var(--muted); display: flex; align-items: center; gap: 9px; }
  .services__item::before { content: ""; width: 6px; height: 6px; border-radius: 50%; background: var(--bullet); }
</style>
</head>
<body>

<section class="postcard postcard--front">
  <h1 class="headline">
    <span class="headline__line headline__line--one">Let Us Help</span>
    <span class="headline__line headline__line--two">Your Business</span>
    <span class="headline__big">SHINE !</span>
  </h1>
  <div class="brand"><span class="brand__dot"></span><span class="brand__name">CardWillow</span></div>
  <div class="photo photo--smile" role="img" aria-label="Close-up of a smile with dental braces"></div>
  <div class="photo photo--model" role="img" aria-label="Beauty portrait of a woman with styled hair"></div>
  <div class="photo photo--car" role="img" aria-label="Headlight of a red sports car"></div>
  <p class="contact">24 hr/ 7day<br>orders@cardwillow.com</p>
</section>

<section class="postcard postcard--back">
  <p class="pitch">Business with no limits, meet mailing with<br>no addresses, gain new customers through<br><span class="pitch__program">"Whole Route Flyer Drop"</span><br>reach new customers at their home<br>without needing their address.</p>

  <div class="indicia">PRSRT STD<br>ECRWSS<br>U.S.Postage<br><span class="indicia__paid">Paid</span><br><span class="indicia__route">WRFD Retail</span></div>
  <div class="address">Local<br>Postal Customer</div>

  <h2 class="specials-title">current<br>specials<br>print</h2>
  <div class="special special--double">Double your<br>order FREE<br>(order 500 business<br>cards and get 1000)</div>
  <div class="special special--brochures">250 100lb gloss<br>stock<br>brochures 99.00</div>
  <div class="special special--packages">Business packages<br>(cards, envelopes<br>and letterhead) 299</div>
  <div class="special special--postcards">5000 postcards<br>179.99</div>
  <div class="special special--flyers">1000 flyers<br>140.40</div>

  <div class="services">
    <h2 class="services__title">Services</h2>
    <ul class="services__list">
      <li class="services__item" style="--bullet:#3aa844">Banners</li>
      <li class="services__item" style="--bullet:#2b92d4">Booklets</li>
      <li class="services__item" style="--bullet:#6a3c96">Brochures</li>
      <li class="services__item" style="--bullet:#d6287c">Business cards</li>
      <li class="services__item" style="--bullet:#2b92d4">Calendars</li>
      <li class="services__item" style="--bullet:#e5262c">Catalogs</li>
      <li class="services__item" style="--bullet:#f05a28">CD/DVD packages</li>
      <li class="services__item" style="--bullet:#f7941d">Envelopes</li>
      <li class="services__item" style="--bullet:#f2e600">Event tickets</li>
      <li class="services__item" style="--bullet:#8cc63e">Flyers</li>
      <li class="services__item" style="--bullet:#1b6b3a">Hangtags</li>
      <li class="services__item" style="--bullet:#1aa39a">Postcards</li>
      <li class="services__item" style="--bullet:#2b92d4">Posters</li>
      <li class="services__item" style="--bullet:#1c2f7a">Presentation folders</li>
      <li class="services__item" style="--bullet:#7a2d8c">Rackcards</li>
      <li class="services__item" style="--bullet:#b5b5b5">Labels</li>
    </ul>
  </div>
</section>

</body>
</html>
```